" O escritório de advocacia atua de forma estratégica e personalizada, oferecendo assessoria jurídica completa com foco na excelência técnica, na ética profissional e na construção de soluções eficazes para seus clientes. O atendimento é conduzido diretamente pelos sócios, garantindo proximidade, confiança e alto nível de especialização em cada demanda. Cada caso é analisado de maneira individualizada, com abordagem analítica, planejamento jurídico preciso e comunicação clara. O escritório combina tradição jurídica e visão contemporânea, utilizando métodos atualizados, organização eficiente e atuação responsável para entregar segurança jurídica e resultados consistentes. "

```html
<!DOCTYPE html>
<html lang="pt-BR">
<head>
<meta charset="UTF-8">
<title>Timbrado — Moreira &amp; Castilho Advogados</title>
<link rel="stylesheet" href="https://fonts.googleapis.com/css2?family=Montserrat:wght@600&display=swap">
<style>
  :root {
    --backdrop: #e9e7e4;
    --paper: #ffffff;
    --brand-grey: #8a8a8c;
    --address-grey: #5c5f66;
    --navy: #13294b;
  }
  html, body {
    margin: 0;
    padding: 0;
    width: 1200px;
    height: 1200px;
    overflow: hidden;
    background: var(--backdrop);
  }
  .canvas {
    position: relative;
    width: 1200px;
    height: 1200px;
  }
  .letterhead {
    position: absolute;
    left: 307px;
    top: 186px;
    width: 586px;
    height: 828px;
    background: var(--paper);
    box-shadow: 0 6px 24px rgba(0, 0, 0, 0.18);
  }
  .brand {
    position: absolute;
    top: 48px;
    left: 0;
    right: 0;
    display: flex;
    justify-content: center;
    align-items: center;
    gap: 8px;
  }
  .brand-mark {
    width: 12px;
    height: 12px;
    background: var(--brand-grey);
  }
  .brand-name {
    margin: 0;
    font-family: "Montserrat", sans-serif;
    font-weight: 600;
    font-size: 15px;
    line-height: 1;
    color: var(--brand-grey);
    white-space: nowrap;
  }
  .address {
    position: absolute;
    left: 0;
    right: 0;
    bottom: 24px;
    margin: 0;
    text-align: center;
    font-family: "Montserrat", sans-serif;
    font-weight: 600;
    font-size: 11px;
    color: var(--address-grey);
    white-space: nowrap;
  }
  .footer-band {
    position: absolute;
    left: 0;
    right: 0;
    bottom: 0;
    height: 12px;
    background: var(--navy);
  }
</style>
</head>
<body>
  <main class="canvas">
    <article class="letterhead">
      <header class="brand">
        <span class="brand-mark" aria-hidden="true"></span>
        <p class="brand-name">Moreira &amp; Castilho Advogados</p>
      </header>
      <p class="address">Rua Aurora, 48 - Sala 705 - Centro - Rio de Janeiro | RJ</p>
      <div class="footer-band"></div>
    </article>
  </main>
</body>
</html>
```